Business Card Design

I need a business card design for a new company that is based in Singapore region. The name of the company is called " Kalvaro Holdings Pte.Ltd " This company serves as a holding company that owns several types of businesses under our name. One of the established company in Singapore is the Kalvaro Food Industries that serves as a food service industry that has their own brand name which operates in malls and CBD areas. We would prefer the design of the business cards will use the colors of black as the base and red as for the designs. The final design of the name card should be able to communicate young and professional type of business culture. In which we appreciate creativity to their highest point.
Industry/Entity Type
Industry
Contact Information for Business Card
Matteo Bastian Kalvaro
Director, Founder
Contact: +65 81247760
E-mail: matteobk@quellmail.com

```html
<!DOCTYPE html>
<html lang="en">
<head>
<meta charset="utf-8">
<title>Kalvaro Holdings – Business Card</title>
<link href="https://fonts.googleapis.com/css2?family=Quicksand:wght@300&family=Roboto:wght@400;700&display=swap" rel="stylesheet">
<style>
  :root {
    --page-bg: #e9e6e1;
    --card-black: #0d0d0e;
    --card-charcoal: #1f2022;
    --brand-red: #d3111c;
    --text-white: #e6e6e6;
    --text-grey: #9a9a9c;
    --silver-light: #f2f2f2;
    --silver-dark: #8a8a8c;
  }
  * { box-sizing: border-box; margin: 0; padding: 0; }
  html, body {
    width: 1200px; height: 784px; overflow: hidden;
    background: var(--page-bg);
  }
  .stage {
    width: 1200px; height: 784px;
    display: flex; align-items: center; justify-content: center; gap: 40px;
  }
  .card {
    position: relative;
    width: 540px; height: 324px;
    background: radial-gradient(ellipse at 40% 35%, var(--card-charcoal), var(--card-black) 75%);
    box-shadow: 0 6px 18px rgba(0,0,0,.25);
    overflow: hidden;
  }
  .wordmark {
    display: flex; align-items: center; gap: 10px;
    font-family: "Roboto", Arial, sans-serif;
    font-weight: 700;
    color: var(--brand-red);
    letter-spacing: .5px;
  }
  .wordmark-square {
    width: 14px; height: 14px; background: var(--brand-red);
  }
  /* Back: contact side */
  .card-contact .wordmark {
    position: absolute; left: 40px; top: 40px;
    font-size: 30px;
  }
  .holder {
    position: absolute; left: 40px; top: 160px;
    font-family: "Roboto", Arial, sans-serif;
  }
  .holder-name {
    color: var(--brand-red); font-weight: 700; font-size: 15px; letter-spacing: .3px;
  }
  .holder-role {
    color: var(--text-white); font-size: 11px; margin-top: 8px;
  }
  .contact-list {
    position: absolute; left: 40px; top: 232px;
    list-style: none;
    font-family: "Roboto", Arial, sans-serif;
    color: var(--text-white); font-size: 16px;
  }
  .contact-list li {
    display: flex; align-items: center; gap: 10px; height: 24px;
  }
  .contact-list svg { width: 16px; height: 16px; flex: none; }
  /* Front: company side */
  .card-company .frame {
    position: absolute; inset: 18px;
    border: 4px solid var(--silver-light);
    border-image: linear-gradient(135deg, var(--silver-dark), var(--silver-light) 35%, var(--silver-dark) 60%, var(--silver-light)) 1;
  }
  .card-company .wordmark {
    position: absolute; left: 0; right: 0; top: 88px;
    justify-content: center;
    font-size: 52px;
  }
  .card-company .wordmark-square { width: 22px; height: 22px; }
  .company-name {
    position: absolute; left: 0; right: 0; top: 222px;
    text-align: center;
    font-family: "Quicksand", "Helvetica Neue", sans-serif;
    font-weight: 300; font-size: 30px;
    color: var(--text-grey); letter-spacing: 1px;
  }
</style>
</head>
<body>
<main class="stage">
  <section class="card card-contact" aria-label="Card back with contact details">
    <div class="wordmark"><span class="wordmark-square"></span>Kalvaro</div>
    <div class="holder">
      <p class="holder-name">Matteo Bastian Kalvaro</p>
      <p class="holder-role">Director, Founder</p>
    </div>
    <ul class="contact-list">
      <li>
        <svg viewBox="0 0 24 24" aria-hidden="true"><path fill="#d3111c" d="M6.6 10.8a15.1 15.1 0 0 0 6.6 6.6l2.2-2.2c.3-.3.7-.4 1-.2 1.1.4 2.3.6 3.6.6.6 0 1 .4 1 1V20c0 .6-.4 1-1 1A17 17 0 0 1 3 4c0-.6.4-1 1-1h3.5c.6 0 1 .4 1 1 0 1.3.2 2.5.6 3.6.1.3 0 .7-.2 1z"/></svg>
        +65 81247760
      </li>
      <li>
        <svg viewBox="0 0 24 24" aria-hidden="true"><rect x="2" y="5" width="20" height="14" rx="2" fill="#d3111c"/><path d="M3 6.5l9 6.5 9-6.5" fill="none" stroke="#0d0d0e" stroke-width="1.8"/></svg>
        matteobk@quellmail.com
      </li>
    </ul>
  </section>

  <section class="card card-company" aria-label="Card front with company name">
    <div class="frame"></div>
    <div class="wordmark"><span class="wordmark-square"></span>Kalvaro</div>
    <p class="company-name">Kalvaro Holdings Pte.Ltd</p>
  </section>
</main>
</body>
</html>
```